Wordpress Design

Need a responsive wordpress website with the minimum 10 service description pages. This website is for a small business consultancy, providing business development and digital marketing services.

Will also need at least 4 diffrent templates: Home page, service page, Landing Page and blog.

The site will be using block editor.

Coded - Design and coding required

1 page

Sans Serif
• Segoe UI

```html
<!DOCTYPE html>
<html lang="en">
<head>
<meta charset="utf-8">
<title>ClearSight Business Consultancy</title>
<link href="https://fonts.googleapis.com/css2?family=Poppins:wght@300;400;500;600;700;800&display=swap" rel="stylesheet">
<style>
:root{
  --blue:#1a9ee8;
  --blue-dark:#0b7fd0;
  --ink:#1e1e1e;
  --text:#3a3a3a;
  --muted:#6b6b6b;
  --grey-bg:#f2f2f2;
  --footer:#141414;
  --white:#ffffff;
}
*{margin:0;padding:0;box-sizing:border-box}
html,body{width:1200px;height:4000px;overflow:hidden}
body{font-family:"Poppins",sans-serif;color:var(--text);background:var(--white);position:relative}
.abs{position:absolute}
.center{text-align:center}

/* header */
.topbar{top:0;left:0;width:1200px;height:93px;background:var(--white)}
.brand{display:flex;align-items:center;gap:12px;font-weight:600;font-size:26px;color:var(--ink)}
.brand .dot{width:40px;height:40px;border-radius:50%;background:var(--blue)}
.contact-item{display:flex;align-items:center;gap:8px;font-size:18px;color:var(--ink)}
.contact-item svg{width:26px;height:26px}
.nav{top:93px;left:0;width:1200px;height:48px;background:var(--blue)}
.nav a{position:absolute;top:13px;color:var(--white);font-size:16px;font-weight:500;text-decoration:none}
.nav .btn{top:5px;left:916px;width:149px;height:39px;background:var(--white);color:var(--ink);border-radius:20px;display:flex;align-items:center;justify-content:center}

/* hero */
.hero{top:141px;left:0;width:1200px;height:665px;background:radial-gradient(ellipse at 45% 40%,#2f4a6a 0%,#15263c 45%,#0a1422 100%)}
.hero-title{left:0;width:1200px;color:var(--white)}
.hero-form{top:575px;left:354px;width:492px;height:44px;display:flex}
.hero-form .field{flex:0 0 320px;background:var(--white);font-size:14px;color:#666;padding:13px 16px}
.hero-form .go{flex:1;background:var(--blue);color:var(--white);font-size:16px;font-weight:500;display:flex;align-items:center;justify-content:center}
.arrow{width:48px;height:48px;border-radius:50%;display:flex;align-items:center;justify-content:center}

/* welcome */
.h2{font-weight:700;color:var(--ink)}
.feature{width:240px;text-align:center}
.feature .ring{width:86px;height:86px;border-radius:50%;border:3px dashed var(--blue);margin:0 auto;display:flex;align-items:center;justify-content:center}
.feature .ring span{width:70px;height:70px;border-radius:50%;background:var(--blue);display:flex;align-items:center;justify-content:center}
.feature h3{font-size:19px;font-weight:500;color:var(--ink);margin-top:18px}
.feature p{width:215px;margin:8px auto 0;font-size:12.5px;line-height:19px;color:var(--muted)}
.divider{width:1px;height:217px;background:#cfcfcf;top:1084px}

/* services */
.services{top:1385px;left:0;width:1200px;height:743px;background:var(--grey-bg)}
.svc{width:216px;height:216px;border-radius:50%;background:var(--white);border:6px solid #f7f7f7;box-shadow:0 6px 16px rgba(0,0,0,.12);text-align:center;padding-top:46px}
.svc svg.ic{width:54px;height:54px}
.svc h4{font-size:16px;font-weight:500;color:var(--ink);line-height:20px;margin-top:10px}
.svc .chev{width:24px;height:24px;margin:10px auto 0}

/* focus */
.focus-list li{list-style:none;display:flex;align-items:center;gap:14px;font-size:16px;font-weight:500;color:var(--ink);height:37px;letter-spacing:.5px}
.dots{display:flex;gap:9px}
.dots i{width:15px;height:15px;border-radius:50%;border:2px solid var(--blue)}
.dots i.on{background:var(--blue)}

/* cta */
.cta{top:2687px;left:0;width:1200px;height:400px;background:linear-gradient(90deg,#1aa3ec,#1ab1f2)}
.cta-btn{top:2946px;left:605px;width:299px;height:53px;border-radius:27px;background:var(--white);color:var(--ink);font-size:18px;display:flex;align-items:center;justify-content:center}

/* news */
.card{top:3207px;width:292px;height:380px;background:var(--white);box-shadow:0 2px 12px rgba(0,0,0,.1)}
.card .img{height:172px}
.card .body{padding:18px 33px}
.card .date{font-size:14px;font-weight:500;color:var(--blue)}
.card h5{font-size:15px;font-weight:600;color:var(--ink);line-height:23px;margin-top:10px;letter-spacing:.4px}
.card p{font-size:13.5px;line-height:19.5px;color:var(--muted);margin-top:8px}
.card .more{font-size:13px;font-weight:600;color:var(--blue);margin-top:10px;display:block}

/* footer */
.footer{top:3653px;left:0;width:1200px;height:347px;background:var(--footer)}
.fcol{top:3715px;color:var(--white)}
.fcol h6{font-size:20px;font-weight:600;letter-spacing:.5px;margin-bottom:10px}
.fcol li{list-style:none;font-size:14.5px;line-height:27px;color:#e0e0e0}
.fline{display:flex;gap:10px;font-size:14.5px;color:#e0e0e0;line-height:18px;margin-bottom:16px}
.social{width:34px;height:34px;border-radius:50%;border:1.5px solid #ddd}
</style>
</head>
<body>

<!-- Header -->
<header class="abs topbar">
  <div class="abs brand" style="top:26px;left:129px"><span class="dot"></span>ClearSight</div>
  <div class="abs contact-item" style="top:32px;left:665px">
    <svg viewBox="0 0 26 26"><circle cx="13" cy="13" r="12" fill="none" stroke="#1a9ee8" stroke-width="1.6"/><path d="M9 8l2 0 1 3-1.3 1a7 7 0 0 0 3.3 3.3l1-1.3 3 1v2a1 1 0 0 1-1 1A10 10 0 0 1 8 9a1 1 0 0 1 1-1z" fill="#1a9ee8"/></svg>
    1 555 014 2266
  </div>
  <div class="abs" style="top:30px;left:850px;width:1px;height:30px;background:#ddd"></div>
  <div class="abs contact-item" style="top:32px;left:868px">
    <svg viewBox="0 0 26 26"><circle cx="13" cy="13" r="12" fill="none" stroke="#1a9ee8" stroke-width="1.6"/><rect x="7" y="9" width="12" height="8" fill="none" stroke="#1a9ee8" stroke-width="1.5"/><path d="M7 9l6 5 6-5" fill="none" stroke="#1a9ee8" stroke-width="1.5"/></svg>
    info@brightmere.ca
  </div>
</header>
<nav class="abs nav">
  <a style="left:132px">HOME</a>
  <a style="left:222px">BUSINESS STRATEGY ⌄</a>
  <a style="left:449px">MARKETING STRATEGY ⌄</a>
  <a style="left:686px">BLOG</a>
  <a style="left:772px">ABOUT US</a>
  <a class="btn">CONTACT US</a>
</nav>

<!-- Hero -->
<section class="abs hero" role="img" aria-label="Hand reaching toward a glowing globe wrapped in a connected network of nodes"></section>
<svg class="abs" style="top:730px;left:0" width="1200" height="80" viewBox="0 0 1200 80">
  <path d="M0 22 Q600 72 1200 22 L1200 80 L0 80Z" fill="#fff"/>
  <path d="M0 22 Q600 72 1200 22" fill="none" stroke="#1a9ee8" stroke-width="7"/>
</svg>
<div class="abs hero-title center" style="top:348px;font-size:24px;font-weight:500">Welcome to ClearSight</div>
<div class="abs hero-title center" style="top:390px;font-size:48px;font-weight:700">BUSINESS CONSULTANCY</div>
<div class="abs hero-title center" style="top:466px;font-size:22px;line-height:32px;font-weight:500">Where your ideas meet our strategy<br>to deliver amazing results</div>
<div class="abs hero-form"><div class="field">Email / Phone</div><div class="go">Get the help Now!</div></div>
<div class="abs arrow" style="top:380px;left:66px;border:2px solid #fff">
  <svg width="20" height="20" viewBox="0 0 20 20"><path d="M13 3L6 10l7 7" fill="none" stroke="#fff" stroke-width="2.2"/></svg>
</div>
<div class="abs arrow" style="top:380px;left:1083px;background:var(--blue)">
  <svg width="20" height="20" viewBox="0 0 20 20"><path d="M7 3l7 7-7 7" fill="none" stroke="#fff" stroke-width="2.2"/></svg>
</div>

<!-- Welcome -->
<h2 class="abs h2 center" style="top:878px;left:0;width:1200px;font-size:40px">Welcome to ClearSight</h2>
<div class="abs" style="top:941px;left:573px;width:54px;height:3px;background:var(--blue)"></div>
<p class="abs center" style="top:960px;left:210px;width:780px;font-size:17px;line-height:27px;color:var(--ink)">Lorem Ipsum is simply dummy text of the printing and typesetting industry. Lorem Ipsum has been the industry's standard dummy text ever since the 1500s, when an unknown printer took a galley of type and scrambled it to make a type specimen book.</p>

<div class="abs feature" style="top:1083px;left:178px">
  <div class="ring"><span><svg width="40" height="40" viewBox="0 0 40 40" fill="none" stroke="#fff" stroke-width="2"><path d="M6 8l6 6M12 8l-6 6M26 26l6 6M32 26l-6 6"/><circle cx="30" cy="11" r="4"/><circle cx="10" cy="29" r="4"/><path d="M14 29c8 0 12-8 12-14"/></svg></span></div>
  <h3>Business Strategy</h3>
  <p>Lorem Ipsum is simply dummy text of the printing and typesetting industry. Lorem Ipsum has been the industry's standard</p>
</div>
<div class="abs divider" style="left:449px"></div>
<div class="abs feature" style="top:1083px;left:476px">
  <div class="ring"><span><svg width="40" height="40" viewBox="0 0 40 40" fill="none" stroke="#fff" stroke-width="2"><circle cx="20" cy="20" r="5"/><circle cx="20" cy="6" r="3"/><circle cx="20" cy="34" r="3"/><circle cx="6" cy="20" r="3"/><circle cx="34" cy="20" r="3"/><circle cx="10" cy="10" r="3"/><circle cx="30" cy="30" r="3"/><circle cx="30" cy="10" r="3"/><circle cx="10" cy="30" r="3"/></svg></span></div>
  <h3>Marketing Strategy</h3>
  <p>Lorem Ipsum is simply dummy text of the printing and typesetting industry. Lorem Ipsum has been the industry's standard</p>
</div>
<div class="abs divider" style="left:748px"></div>
<div class="abs feature" style="top:1083px;left:780px">
  <div class="ring"><span><svg width="40" height="40" viewBox="0 0 40 40" fill="none" stroke="#fff" stroke-width="2"><circle cx="20" cy="20" r="13"/><path d="M20 12a6 6 0 0 0-3 11v3h6v-3a6 6 0 0 0-3-11zM17 29h6"/></svg></span></div>
  <h3>Advertising</h3>
  <p>Lorem Ipsum is simply dummy text of the printing and typesetting industry. Lorem Ipsum has been the industry's standard</p>
</div>

<!-- Services -->
<section class="abs services"></section>
<p class="abs center" style="top:1455px;left:0;width:1200px;font-size:25px;line-height:37px;font-weight:500;color:var(--ink)">All our efforts are concentrated on reaching your<br>customers where they ar getting you closer to you customers</p>

<div class="abs svc" style="top:1577px;left:133px">
  <svg class="ic" viewBox="0 0 54 54" fill="none" stroke="#222" stroke-width="2"><rect x="6" y="4" width="42" height="16"/><path d="M11 10h20M11 14h28"/><circle cx="17" cy="32" r="5"/><circle cx="37" cy="32" r="5"/><path d="M8 48c0-7 18-7 18 0M28 48c0-7 18-7 18 0"/></svg>
  <h4>Business Consultancy<br>and Advisory</h4>
  <svg class="chev" viewBox="0 0 24 24"><circle cx="12" cy="12" r="10" fill="none" stroke="#1a9ee8" stroke-width="1.3"/><path d="M8 10l4 4 4-4" fill="none" stroke="#1a9ee8" stroke-width="1.5"/></svg>
</div>
<div class="abs svc" style="top:1577px;left:372px">
  <svg class="ic" viewBox="0 0 54 54" fill="none" stroke="#222" stroke-width="2"><rect x="8" y="6" width="16" height="14"/><rect x="28" y="4" width="18" height="14"/><path d="M32 14v-4M36 14v-6M40 14v-3"/><rect x="8" y="28" width="12" height="10"/><rect x="32" y="28" width="12" height="10"/><path d="M20 33h12M26 20v8M16 42v6M38 42v6"/></svg>
  <h4>Business Plan<br>Development</h4>
  <svg class="chev" viewBox="0 0 24 24"><circle cx="12" cy="12" r="10" fill="none" stroke="#1a9ee8" stroke-width="1.3"/><path d="M8 10l4 4 4-4" fill="none" stroke="#1a9ee8" stroke-width="1.5"/></svg>
</div>
<div class="abs svc" style="top:1577px;left:611px">
  <svg class="ic" viewBox="0 0 54 54" fill="none" stroke="#222" stroke-width="2"><path d="M4 48h46"/><rect x="8" y="34" width="7" height="14"/><rect x="19" y="28" width="7" height="20"/><rect x="30" y="22" width="7" height="26"/><rect x="41" y="16" width="7" height="32"/><path d="M6 26L22 14l8 6L46 4M40 4h6v6"/></svg>
  <h4>Profit and Growth<br>Improvement</h4>
  <svg class="chev" viewBox="0 0 24 24"><circle cx="12" cy="12" r="10" fill="none" stroke="#1a9ee8" stroke-width="1.3"/><path d="M8 10l4 4 4-4" fill="none" stroke="#1a9ee8" stroke-width="1.5"/></svg>
</div>
<div class="abs svc" style="top:1577px;left:850px">
  <svg class="ic" viewBox="0 0 54 54" fill="none" stroke="#222" stroke-width="2"><rect x="4" y="4" width="46" height="18"/><path d="M9 10h36M9 15h26"/><path d="M8 32h6l12-6v20l-12-6H8z"/><rect x="32" y="34" width="16" height="12"/><path d="M36 34v-4h8v4"/></svg>
  <h4>Marketing Consultancy<br>and Advisory</h4>
  <svg class="chev" viewBox="0 0 24 24"><circle cx="12" cy="12" r="10" fill="none" stroke="#1a9ee8" stroke-width="1.3"/><path d="M8 10l4 4 4-4" fill="none" stroke="#1a9ee8" stroke-width="1.5"/></svg>
</div>

<div class="abs svc" style="top:1818px;left:133px">
  <svg class="ic" viewBox="0 0 54 54" fill="none" stroke="#222" stroke-width="2"><path d="M4 20l4-14h38l4 14z" fill="#222"/><path d="M8 22v26h38V22"/><rect x="22" y="32" width="10" height="16"/></svg>
  <h4>Brand Building<br>and Strategy</h4>
  <svg class="chev" viewBox="0 0 24 24"><circle cx="12" cy="12" r="10" fill="none" stroke="#1a9ee8" stroke-width="1.3"/><path d="M8 10l4 4 4-4" fill="none" stroke="#1a9ee8" stroke-width="1.5"/></svg>
</div>
<div class="abs svc" style="top:1818px;left:372px">
  <svg class="ic" viewBox="0 0 54 54" fill="none" stroke="#222" stroke-width="2"><circle cx="10" cy="10" r="5"/><circle cx="44" cy="10" r="5"/><circle cx="10" cy="44" r="5"/><circle cx="44" cy="44" r="5"/><circle cx="27" cy="27" r="7"/><path d="M17 10h20M10 17v20M44 17v20M17 44h20" stroke-dasharray="3 3"/></svg>
  <h4>Customer Experience<br>Mapping</h4>
  <svg class="chev" viewBox="0 0 24 24"><circle cx="12" cy="12" r="10" fill="none" stroke="#1a9ee8" stroke-width="1.3"/><path d="M8 10l4 4 4-4" fill="none" stroke="#1a9ee8" stroke-width="1.5"/></svg>
</div>
<div class="abs svc" style="top:1818px;left:611px">
  <svg class="ic" viewBox="0 0 54 54" fill="none" stroke="#222" stroke-width="2"><circle cx="27" cy="27" r="20"/><path d="M7 27h40M27 7c-8 8-8 32 0 40M27 7c8 8 8 32 0 40"/><circle cx="38" cy="38" r="8" fill="#222"/></svg>
  <h4>Digital Footprint<br>Optimisation</h4>
  <svg class="chev" viewBox="0 0 24 24"><circle cx="12" cy="12" r="10" fill="none" stroke="#1a9ee8" stroke-width="1.3"/><path d="M8 10l4 4 4-4" fill="none" stroke="#1a9ee8" stroke-width="1.5"/></svg>
</div>
<div class="abs svc" style="top:1818px;left:850px">
  <svg class="ic" viewBox="0 0 54 54" fill="none" stroke="#222" stroke-width="2"><circle cx="27" cy="27" r="17"/><circle cx="27" cy="24" r="5"/><path d="M19 38c2-6 14-6 16 0M27 4v8M27 42v8M4 27h8M42 27h8"/></svg>
  <h4>Advertising<br>Services</h4>
  <svg class="chev" viewBox="0 0 24 24"><circle cx="12" cy="12" r="10" fill="none" stroke="#1a9ee8" stroke-width="1.3"/><path d="M8 10l4 4 4-4" fill="none" stroke="#1a9ee8" stroke-width="1.5"/></svg>
</div>

<!-- Focus -->
<svg class="abs" style="top:2128px;left:606px" width="594" height="559" viewBox="0 0 594 559" role="img" aria-label="Hands holding a tablet with floating business charts over a blue server room">
  <defs><linearGradient id="focusFill" x1="0" y1="0" x2="1" y2="1"><stop offset="0" stop-color="#5a86b0"/><stop offset=".5" stop-color="#1d3e66"/><stop offset="1" stop-color="#0e2440"/></linearGradient></defs>
  <path d="M130 0 Q-20 150 10 320 Q40 480 140 559 L594 559 L594 0Z" fill="url(#focusFill)"/>
  <path d="M130 0 Q-20 150 10 320 Q40 480 140 559" fill="none" stroke="#111" stroke-width="6"/>
</svg>
<h2 class="abs h2" style="top:2224px;left:132px;font-size:29px;line-height:40px">FOCUS ON WHAT MATTERS<br>THE MOST</h2>
<p class="abs" style="top:2318px;left:132px;width:420px;font-size:15px;line-height:26px;color:var(--ink)">Grow your traffic and contribute more pipeline with a suite of services designed to deliver ideal prospects to sales</p>
<ul class="abs focus-list" style="top:2417px;left:132px">
  <li><svg width="24" height="24" viewBox="0 0 24 24" fill="none" stroke="#222" stroke-width="1.8"><path d="M21 12a9 9 0 1 1-4-7.5"/><path d="M8 11l4 4 9-10"/></svg>PURCHASE</li>
  <li><svg width="24" height="24" viewBox="0 0 24 24" fill="none" stroke="#222" stroke-width="1.8"><path d="M21 12a9 9 0 1 1-4-7.5"/><path d="M8 11l4 4 9-10"/></svg>CONSIDERATION</li>
  <li><svg width="24" height="24" viewBox="0 0 24 24" fill="none" stroke="#222" stroke-width="1.8"><path d="M21 12a9 9 0 1 1-4-7.5"/><path d="M8 11l4 4 9-10"/></svg>INTEREST</li>
  <li><svg width="24" height="24" viewBox="0 0 24 24" fill="none" stroke="#222" stroke-width="1.8"><path d="M21 12a9 9 0 1 1-4-7.5"/><path d="M8 11l4 4 9-10"/></svg>AWARENESS</li>
</ul>
<div class="abs dots" style="top:2617px;left:271px"><i></i><i class="on"></i><i></i><i></i></div>

<!-- CTA -->
<section class="abs cta"></section>
<svg class="abs" style="top:2687px;left:0" width="460" height="400" viewBox="0 0 460 400" role="img" aria-label="Two colleagues working together at a laptop in an office">
  <defs><linearGradient id="ctaPhoto" x1="0" y1="0" x2="1" y2="0"><stop offset="0" stop-color="#d9dde2"/><stop offset=".6" stop-color="#b9c3cf"/><stop offset="1" stop-color="#5d7796"/></linearGradient></defs>
  <path d="M0 0 L378 0 Q300 160 410 400 L0 400Z" fill="url(#ctaPhoto)"/>
  <path d="M378 0 Q300 160 410 400" fill="none" stroke="#fff" stroke-width="5"/>
</svg>
<h2 class="abs" style="top:2766px;left:605px;font-size:29px;line-height:41px;font-weight:400;color:var(--white)"><strong style="font-weight:700">Ready to transform</strong> your business<br>process and marketing efforts?</h2>
<p class="abs" style="top:2861px;left:605px;font-size:18px;line-height:30px;color:var(--white)">Request a free assessment and<br>get started today</p>
<div class="abs cta-btn">Request a free consultation</div>

<!-- News -->
<h2 class="abs h2 center" style="top:3132px;left:0;width:1200px;font-size:33px">LATEST NEWS</h2>
<article class="abs card" style="left:132px">
  <div class="img" role="img" aria-label="Glowing digital padlock floating above an open hand" style="background:radial-gradient(circle at 50% 45%,#4fb3c9,#14475e 55%,#08202d)"></div>
  <div class="body"><div class="date">JAN 20, 2020</div><h5>INDUSTRY'S STANDARD<br>DUMMY TEXT EVER</h5><p>Lorem Ipsum is simply dummy text of the printing &amp; typesetting industry. Lorem Ipsum</p><span class="more">LEARN MORE ›</span></div>
</article>
<article class="abs card" style="left:453px">
  <div class="img" role="img" aria-label="Laptop with glowing bar chart rising above a desk" style="background:linear-gradient(160deg,#6a7078,#2b2e33 55%,#8a6a2a)"></div>
  <div class="body"><div class="date">JAN 20, 2020</div><h5>INDUSTRY'S STANDARD<br>DUMMY TEXT EVER</h5><p>Lorem Ipsum is simply dummy text of the printing &amp; typesetting industry. Lorem Ipsum</p><span class="more">LEARN MORE ›</span></div>
</article>
<article class="abs card" style="left:775px">
  <div class="img" role="img" aria-label="Blue glowing security shield on a digital background" style="background:radial-gradient(circle at 45% 50%,#3b7cf0,#123a9a 55%,#0a1c55)"></div>
  <div class="body"><div class="date">JAN 20, 2020</div><h5>INDUSTRY'S STANDARD<br>DUMMY TEXT EVER</h5><p>Lorem Ipsum is simply dummy text of the printing &amp; typesetting industry. Lorem Ipsum</p><span class="more">LEARN MORE ›</span></div>
</article>

<!-- Footer -->
<footer class="abs footer"></footer>
<div class="abs fcol" style="left:132px"><h6>COMPANY</h6><ul><li>Home</li><li>About Us</li><li>Business Strategy</li><li>Marketing Strategy</li><li>Blog</li></ul></div>
<div class="abs fcol" style="left:343px"><h6>RESOURCES</h6><ul><li>About Us</li><li>Sitemap</li><li>Career</li><li>Cotact Us</li><li>Tearms</li></ul></div>
<div class="abs fcol" style="left:545px"><h6>CONTACT US</h6>
  <div class="fline"><svg width="14" height="18" viewBox="0 0 14 18"><path d="M7 0a6 6 0 0 0-6 6c0 5 6 12 6 12s6-7 6-12a6 6 0 0 0-6-6z" fill="#fff"/><circle cx="7" cy="6" r="2.2" fill="#141414"/></svg><span>240 Elm Street #4B<br>Texas 20012 TX</span></div>
  <div class="fline"><svg width="16" height="16" viewBox="0 0 16 16"><path d="M3 1l3 0 1 4-2 1.5a9 9 0 0 0 4.5 4.5L11 9l4 1v3a2 2 0 0 1-2 2A13 13 0 0 1 1 3a2 2 0 0 1 2-2z" fill="#fff"/></svg><span>(555) 014 2266</span></div>
  <div class="fline"><svg width="16" height="14" viewBox="0 0 16 14"><rect x="0" y="1" width="16" height="12" fill="#fff"/><path d="M0 1l8 6 8-6" fill="none" stroke="#141414" stroke-width="1.4"/></svg><span>info@clearsight-mail.com</span></div>
</div>
<div class="abs brand" style="top:3752px;left:831px;color:#fff"><span class="dot"></span>ClearSight</div>
<div class="abs" style="top:3817px;left:874px;display:flex;gap:6px"><span class="social"></span><span class="social"></span><span class="social"></span><span class="social"></span></div>
<div class="abs" style="top:3920px;left:0;width:1200px;height:1px;background:#333"></div>
<p class="abs center" style="top:3936px;left:0;width:1200px;font-size:14px;color:#ddd">© 2020 ClearSight. All Rights are Reserved.</p>

</body>
</html>
```